Health care center needs brochure design

We need a set of brochure designs for the 4 sections of our clinic, color coded based on the brand guidelines and with introduced icons to every section. The three sections include Biological Medicine (main medication tool is the IV tool), The Brindle Path program (main medication tool are the detox tools) , the Aesthetics section ( main medication tool is the syringe) and the lab (main tool is the microscope). You can find out more about our sections in the website www.velnortaclinic-example.com. The use of elements of the brand itself such as the lotus is also applicable.

Industry/Entity Type

Health Care

Requirements
Must have
• use of brand identity colors and features
• reflective medical icons
• color coding for each of the 4 sections based on the brand colors
Should not have
• pictures overused by other health care providers

```html
<!DOCTYPE html>
<html lang="en">
<head>
<meta charset="utf-8">
<title>Velnorta Integrated Care Center – Brochure</title>
<link href="https://fonts.googleapis.com/css2?family=Montserrat:wght@300;400;500;600&display=swap" rel="stylesheet">
<style>
:root{
  --page:#eceae6;
  --cover:#b6d4ef;
  --cover-back:#a9cbea;
  --white:#ffffff;
  --ink:#7a7a7a;
  --ink-dark:#555a60;
  --green:#72c7ab;
  --green-text:#5fbb9b;
  --pink:#e5bab2;
  --pink-text:#e09a8e;
  --orange:#f7b48c;
  --orange-text:#f2a27a;
  --blue:#c2d3f0;
  --blue-text:#8eaede;
  --rule:#d9d9d9;
}
*{box-sizing:border-box;margin:0;padding:0}
html,body{width:1200px;height:2525px;overflow:hidden}
body{background:var(--page);font-family:"Montserrat",sans-serif;color:var(--ink);position:relative}
.panel{position:absolute;left:53px;width:1094px;background:var(--white);box-shadow:0 2px 6px rgba(0,0,0,.12);overflow:hidden}

/* cover */
.cover{top:50px;height:775px;background:var(--cover)}
.cover-back{position:absolute;left:0;top:0;width:547px;height:100%;background:var(--cover-back)}
.brand{display:flex;align-items:center;gap:8px;font-weight:500;letter-spacing:.5px}
.brand-dot{width:14px;height:14px;border-radius:50%;flex:none}
.cover .brand-small{position:absolute;left:40px;top:50px;color:var(--white);font-size:13px}
.cover .brand-small .brand-dot{background:var(--white)}
.map-area{position:absolute;left:39px;top:241px;width:468px;height:298px;background:linear-gradient(135deg,#e8eef2,#cfe2f2 55%,#eef0ea);border:2px solid var(--white)}
.address{position:absolute;left:39px;top:580px;color:var(--white);font-size:19px;line-height:23px;font-weight:300}
.address .name{font-weight:500;font-size:21px}
.address .phone{font-size:36px;font-weight:600;line-height:46px;margin-top:4px}
.address .email{font-size:18px;color:var(--ink-dark)}
.cover-brand{position:absolute;left:640px;top:370px;color:var(--white);font-size:20px;line-height:24px}
.cover-brand .brand-dot{width:70px;height:70px;background:var(--white);opacity:.85}
.cover-brand .brand{gap:18px}

/* inner spreads */
.spread{display:grid;grid-template-columns:547px 1fr;grid-template-rows:163px 204px 1fr}
.spread-one{top:867px;height:769px}
.spread-two{top:1678px;height:773px}
.topbar{grid-column:1 / 3;position:relative}
.topbar .brand{position:absolute;left:40px;top:55px;font-size:12px;color:var(--ink)}
.topbar .brand-dot{background:var(--green)}
.divider{position:absolute;top:38px;width:1px;height:90px;background:var(--rule)}
.icon{position:absolute;top:30px;width:90px;height:100px}
.feature{padding:30px 40px 0 40px;color:var(--white)}
.feature h2{font-size:19px;font-weight:500;letter-spacing:.6px;margin-bottom:14px}
.feature p{font-size:12px;line-height:14px;font-weight:300}
.green{background:var(--green)}
.orange{background:var(--orange)}
.intro{padding:20px 40px 0 38px}
.intro h2{font-size:19px;font-weight:400;letter-spacing:.6px;margin-bottom:16px}
.intro p{font-size:12.5px;line-height:14.5px;color:var(--ink)}
.pink-head h2{color:var(--pink-text)}
.blue-head h2{color:var(--blue-text)}
.lists{display:flex;gap:40px;padding:34px 30px 0 40px}
.list h3{font-size:15px;font-weight:500;letter-spacing:.5px;line-height:18px}
.list h3::after{content:"";display:block;width:64px;height:1px;background:currentColor;opacity:.5;margin:12px 0 10px}
.list li{list-style:none;font-size:14.5px;line-height:24.5px;font-weight:300;white-space:nowrap}
.list .sub{font-weight:500;margin-top:6px}
.list .sub:first-child{margin-top:0}
.green-list{color:var(--green-text)}
.orange-lists{gap:14px;padding:34px 10px 0 38px}
.orange-list{color:var(--orange-text)}
.orange-list:first-child{width:262px;flex:none}
.orange-list li{line-height:20.5px;font-size:13.5px}
.conditions{position:relative;padding:34px 40px 0 150px}
.conditions.pink{background:var(--pink);color:var(--ink)}
.conditions.blue{background:var(--blue);color:var(--white)}
.conditions .list li{line-height:24.5px}
.corner-brand{position:absolute;right:40px;bottom:40px;font-size:10px}
.conditions.pink .corner-brand{color:var(--white)}
.conditions.blue .corner-brand{color:var(--white)}
.corner-brand .brand-dot{width:20px;height:20px;background:var(--white)}
</style>
</head>
<body>

<section class="panel cover">
  <div class="cover-back"></div>
  <div class="brand brand-small"><span class="brand-dot"></span>VELNORTA INTEGRATED CARE CENTER</div>
  <div class="map-area" role="img" aria-label="Street map showing the clinic location by the marina"></div>
  <div class="address">
    <div class="name">Velnorta Integrated Care Center</div>
    <div>PO Box 40210</div>
    <div>Harbor District, Marina Quarter</div>
    <div>United Arab Emirates</div>
    <div class="phone">02-555 0147</div>
    <div class="email">info@velnortaclinic-example.com</div>
  </div>
  <div class="cover-brand">
    <div class="brand"><span class="brand-dot"></span><span>VELNORTA<br>INTEGRATED<br>CARE CENTER</span></div>
  </div>
</section>

<section class="panel spread spread-one">
  <div class="topbar">
    <div class="brand"><span class="brand-dot"></span>VELNORTA INTEGRATED CARE CENTER</div>
    <span class="divider" style="left:417px"></span>
    <svg class="icon" style="left:440px" viewBox="0 0 90 100" fill="none" stroke="#72c7ab" stroke-width="2">
      <rect x="25" y="12" width="40" height="55" rx="6"/>
      <line x1="45" y1="4" x2="45" y2="12"/>
      <line x1="33" y1="32" x2="45" y2="32"/><line x1="33" y1="42" x2="45" y2="42"/><line x1="33" y1="52" x2="45" y2="52"/>
      <rect x="40" y="67" width="10" height="10"/>
      <line x1="45" y1="77" x2="45" y2="98"/>
    </svg>
    <span class="divider" style="left:931px"></span>
    <div class="icon" style="left:968px;background:linear-gradient(135deg,#f3ddd8,#e5bab2)" role="img" aria-label="Line illustration of detox seed pods"></div>
  </div>
  <div class="feature green">
    <h2>BIOLOGICAL MEDICINE</h2>
    <p>The Center provides a combination of therapies and diagnostics relevent to each individuals case. It is recomended that the patient passes through consultation prior to going through any type of treatment as the practitioner studies thoroughly specific elements of the persons condition and directs them towards the best therapy course.</p>
  </div>
  <div class="intro pink-head">
    <h2>THE BRINDLE PATH PROGRAM</h2>
    <p>Maintaining a healthy lifestyle is a personal goal for everyone, whether you have had a treatment for something or simply wish to ensure you are always at a healthy natural state, the center will help facilitate that. Maintaining health is the way to control your body weight, have an amazing skin, and avoid risks of getting diseases. Releasing toxins and negative energy revives the body's internal health and naturally reflects on its organic system. A set of detox and nutritional programs in addition to tapping and sound therapies are provided by the center for your satisfaction and health from within.</p>
  </div>
  <div class="lists">
    <div class="list green-list">
      <h3>WE SPECIALIZE IN</h3>
      <ul>
        <li>General Medical Consultation</li><li>Healthy Lifestyle consultation</li><li>Magnetic Field Therapy</li><li>Detoxification using Pressotherapy</li><li>Orthomolecular concepts</li><li>Nutritional consultations</li><li>Kinesiology, body mind therapy</li><li>IV's immune syst. stimulation (Vit. C)</li><li>Chelation IV</li><li>Neural therapy, injections</li><li>Lymphatic Drainage</li><li>Manual massages</li>
      </ul>
    </div>
    <div class="list green-list">
      <h3>OUR DIAGNOSTICS<br>INCLUDE</h3>
      <ul>
        <li>Body check up</li><li>Darkfield microscopy</li><li>Mineral scan</li><li>Heart rate variability</li><li>Lab: heavy metal lab</li><li>Lab: hormones</li><li>Lab: stool test</li><li>Lab: fatty acid profiles</li><li>Lab: food intolerance test</li>
      </ul>
    </div>
  </div>
  <div class="conditions pink">
    <div class="list">
      <h3>CONDITIONS WE TREAT</h3>
      <ul>
        <li>Weight loss/gain</li><li>Digestive Conditions</li><li>Skin Conditions</li><li>Chronic Headaches and Migraines</li><li>Fatigue and Insomnia</li><li>Allergies</li><li>Depression</li><li>Joints Conditions</li><li>Muscle Conditions</li><li>Neural Conditions</li><li>Hyperacidity</li>
      </ul>
    </div>
    <div class="brand corner-brand"><span class="brand-dot"></span>VELNORTA</div>
  </div>
</section>

<section class="panel spread spread-two">
  <div class="topbar">
    <div class="brand"><span class="brand-dot"></span>VELNORTA INTEGRATED CARE CENTER</div>
    <span class="divider" style="left:364px"></span>
    <svg class="icon" style="left:385px" viewBox="0 0 90 100" fill="none" stroke="#f2a27a" stroke-width="2">
      <g transform="rotate(-40 45 50)">
        <rect x="35" y="28" width="20" height="50" rx="2"/>
        <line x1="45" y1="78" x2="45" y2="98"/>
        <line x1="45" y1="4" x2="45" y2="28"/>
        <line x1="33" y1="4" x2="57" y2="4"/>
        <line x1="35" y1="40" x2="43" y2="40"/><line x1="35" y1="50" x2="43" y2="50"/><line x1="35" y1="60" x2="43" y2="60"/>
      </g>
    </svg>
    <span class="divider" style="left:931px"></span>
    <svg class="icon" style="left:975px" viewBox="0 0 90 100" fill="none" stroke="#9bb5e0" stroke-width="2">
      <rect x="38" y="8" width="12" height="34" rx="2" transform="rotate(-20 44 25)"/>
      <path d="M30 55 h30"/>
      <path d="M58 40 a22 22 0 0 1 -6 42"/>
      <line x1="45" y1="42" x2="45" y2="55"/>
      <rect x="20" y="82" width="55" height="10"/>
    </svg>
  </div>
  <div class="feature orange">
    <h2>AESTHETICS</h2>
    <p>We like to see you glowing inside out, so to compliment our holistic services we provide the latest Aesthetic skin care technologies and treatments. The center provides unique blends of vitamins and minerals for skin rejuvenation. Beauty comes from within, adding a bit care to boost your spirit and look glamorous is a plus we thrive to provide.</p>
  </div>
  <div class="intro blue-head">
    <h2>DIAGNOSTICS AND TREATMENTS</h2>
    <p>Maintaining a healthy lifestyle is a personal goal for everyone, whether you have had a treatment for something or simply wish to ensure you are always at a healthy natural state, the center will help facilitate that. Maintaining health is the way to control your body weight, have an amazing skin, and avoid risks of getting diseases. Releasing toxins and negative energy revives the body's internal health and naturally reflects on its organic system. A set of detox</p>
  </div>
  <div class="lists orange-lists">
    <div class="list orange-list">
      <h3>OUR TREATMENTS INCLUDE</h3>
      <ul>
        <li class="sub">Face Treatment</li>
        <li>Crystal Peeling</li><li>Face Lifting - PRP</li><li>Anti-Wrinkle and Lip treatment</li><li>Puffy Eye Treatment</li><li>Acne Treatment alternatives</li><li>Mesotherapy</li><li>Lumen Skin Micro-needling</li><li>Stem Cell Serum&nbsp; Micro-needling</li><li>LED Light therapy face mask</li><li>Oxygen/Hyaluronic Acid Infusion</li><li>Hydra-Dermabrasion</li><li>Micro-Dermabrasion</li>
      </ul>
    </div>
    <div class="list orange-list">
      <ul>
        <li class="sub">Body Treatment</li>
        <li>Slimming and Body Firming</li><li>Fat Freeze (Cryolipolysis)</li>
        <li class="sub">Hair Treatments</li>
        <li>Hair restoration treatment<br>with Lumen Skin</li><li>Hair reduction treatment<br>with Laser Technology</li><li>Eye Lash Enhancer</li>
      </ul>
    </div>
  </div>
  <div class="conditions blue">
    <div class="list">
      <h3>CONDITIONS WE TREAT</h3>
      <ul>
        <li>Weight loss/gain</li><li>Digestive Conditions</li><li>Skin Conditions</li><li>Chronic Headaches and Migraines</li><li>Fatigue and Insomnia</li><li>Allergies</li><li>Depression</li><li>Joints Conditions</li><li>Muscle Conditions</li><li>Neural Conditions</li><li>Hyperacidity</li>
      </ul>
    </div>
    <div class="brand corner-brand"><span class="brand-dot"></span>VELNORTA</div>
  </div>
</section>

</body>
</html>
```